Email Design For Quietgrove Trust

Need an email designed for a funeral home company called Quietgrove Trust.
Final design needs to be delivered in HTML5 but can mock up design in any format.

CONCEPT/THEME

Design email for Pre-Planning Funeral Arrangements
Company is called Quietgrove Trust Cemeteries and Funeral Homes

Email will target consumers that are interested in pre-planning for their funeral arrangements.

```html
<!DOCTYPE html>
<html lang="en">
<head>
<meta charset="utf-8">
<title>Quietgrove Trust – Planning Ahead</title>
<link href="https://fonts.googleapis.com/css2?family=Lobster&family=Open+Sans:wght@400;600;700;800&display=swap" rel="stylesheet">
<style>
:root{
  --yellow:#f4ea7b;
  --plum:#8c1c6c;
  --purple:#6a2a7d;
  --magenta:#c9146f;
  --orange:#d83c16;
  --brown:#9b6b3c;
  --green:#2e9a2a;
  --green-dark:#1d6e1a;
  --ink:#1d1d1d;
  --grey:#555;
  --gold:#8b7348;
  --white:#fff;
  --tint:rgba(255,255,255,.22);
}
*{margin:0;padding:0;box-sizing:border-box}
html,body{width:1200px;height:3433px;overflow:hidden;background:var(--white)}
body{position:relative;font-family:"Open Sans",sans-serif;color:var(--ink)}
.abs{position:absolute}
.yellow-field{left:0;top:575px;width:1200px;height:1840px;background:var(--yellow)}
.hero-photo{left:0;top:120px;width:1200px;height:455px;background:linear-gradient(180deg,#8fb0d8 0%,#c9d6e4 45%,#e3dcd0 65%,#6f8f4a 100%)}
.hero-rule{left:0;top:116px;width:1200px;height:5px;background:var(--yellow)}
.brand-box{left:103px;top:31px;width:252px;height:184px;background:var(--white);box-shadow:0 2px 8px rgba(0,0,0,.25);display:flex;align-items:center;justify-content:center}
.brand-name{font-weight:700;color:#1f3a8a;font-size:30px}
.headline{left:146px;top:650px;font-family:"Lobster",sans-serif;font-weight:400;color:var(--plum);font-size:76px;line-height:76px}
.intro{left:148px;top:846px;width:700px;font-size:23px;line-height:32px}
.cup{left:934px;top:857px;width:266px;height:214px;background:#efe9dc}
.flowers{left:0;top:1097px;width:180px;height:790px;background:#d9955a}
.card{left:135px;width:928px;height:246px;border-radius:6px;box-shadow:0 4px 8px rgba(0,0,0,.25);color:var(--white)}
.card-purple{top:1118px;background:var(--purple)}
.card-magenta{top:1392px;background:var(--magenta)}
.card-orange{top:1671px;background:var(--orange)}
.card-brown{top:1951px;background:var(--brown)}
.card-title{position:absolute;left:265px;width:600px;font-family:"Lobster",sans-serif;font-weight:400;font-size:46px;line-height:48px}
.card-text{position:absolute;left:265px;width:545px;font-size:21px;line-height:29px}
.card-icon{position:absolute;left:66px;top:50%;width:130px;height:130px;transform:translateY(-50%);background:var(--tint);border-radius:8px}
.feather{position:absolute;right:8px;top:-20px;width:150px;height:110px;background:var(--tint)}
.ribbon{left:140px;top:2335px;width:892px;height:250px}
.call-circle{left:540px;top:2233px;width:120px;height:120px;border-radius:50%;background:var(--green-dark);border:6px solid #123f10;display:flex;align-items:center;justify-content:center}
.call-lines{left:0;width:1200px;text-align:center;color:var(--white);font-weight:800}
.call-head{top:2383px;font-size:30px;line-height:40px;letter-spacing:.5px}
.call-number{top:2470px;font-size:60px;line-height:80px;letter-spacing:1px}
.promo{left:0;top:2640px;width:1200px;text-align:center;font-weight:700;color:var(--grey);font-size:28px;line-height:40px}
.location{left:115px;top:2804px;width:980px;height:299px;border:2px solid #d8cfa8;border-radius:20px;overflow:hidden;background:var(--white)}
.location-photo{position:absolute;left:0;top:0;width:345px;height:100%;background:linear-gradient(180deg,#7ea0cf 0%,#dfe6ee 50%,#e8ddc9 68%,#4f7a2e 100%)}
.location-body{position:absolute;left:402px;top:40px;color:var(--gold)}
.location-title{font-size:38px;font-weight:600;margin-bottom:18px}
.location-name{font-size:22px;font-weight:600;margin-bottom:8px}
.location-line{font-size:22px;line-height:34px;color:#7d6a47}
.learn{left:0;top:3160px;width:1200px;text-align:center;font-size:26px;color:var(--gold)}
.social{top:3228px;width:120px;height:118px;border-radius:16px;background:var(--gold);display:flex;align-items:center;justify-content:center;color:var(--white);font-weight:700;font-size:22px}
.social-web{left:456px}
.social-follow{left:626px}
</style>
</head>
<body>
<div class="abs yellow-field"></div>
<div class="abs hero-photo" role="img" aria-label="Photo of the cemetery's white arched entrance gate under a cloudy sky with palm trees"></div>
<div class="abs hero-rule"></div>
<div class="abs brand-box"><span class="brand-name">Palm Hollow</span></div>

<h1 class="abs headline">Planning ahead can make<br>all the difference</h1>
<p class="abs intro">It’s not easy to talk about your end-of-life wishes before you have to. But it’s one of the most important conversations you’ll ever have with your loved ones. By preplanning your funeral, you can make sure your life is celebrated the way you want, and give your loved ones the peace-of-mind they need when the time comes.</p>
<div class="abs cup" role="img" aria-label="Photo of a white coffee cup on a saucer"></div>
<div class="abs flowers" role="img" aria-label="Photo of a bouquet of orange lilies and carnations"></div>

<section class="abs card card-purple">
  <div class="card-icon" role="img" aria-label="Illustration of a notebook with a pen"></div>
  <div class="feather" role="img" aria-label="White feather ornament"></div>
  <h2 class="card-title" style="top:40px">Put your wishes in writing</h2>
  <p class="card-text" style="top:113px">You want your funeral to be meaningful, right? By sharing your end-of-life wishes, you’ll ensure your funeral will truly reflect you and your life.</p>
</section>

<section class="abs card card-magenta">
  <div class="card-icon" role="img" aria-label="Illustration of hands holding a heart"></div>
  <div class="feather" role="img" aria-label="White feather ornament"></div>
  <h2 class="card-title" style="top:38px">Eliminate stress for your<br>loved ones</h2>
  <p class="card-text" style="top:142px">By prearranging your funeral, you can alleviate the stress and burden of making tough decisions at an already difficult time for them.</p>
</section>

<section class="abs card card-orange">
  <div class="card-icon" role="img" aria-label="Illustration of a clock with a dollar coin"></div>
  <div class="feather" role="img" aria-label="White feather ornament"></div>
  <h2 class="card-title" style="top:36px">Save time and money</h2>
  <p class="card-text" style="top:108px">Protect your loved ones from inflation by locking in today’s prices for the funeral you truly want. Your expenses will be taken care of when you need them to be, guaranteed.</p>
</section>

<section class="abs card card-brown">
  <div class="card-icon" role="img" aria-label="Illustration of a feather in a circle"></div>
  <div class="feather" role="img" aria-label="White feather ornament"></div>
  <h2 class="card-title" style="top:35px">Personalize your service</h2>
  <p class="card-text" style="top:107px">It’s your funeral, so celebrate your life, your way. By preplanning, you can choose your own funeral services, including songs, readings or other personal details that are important to you.</p>
</section>

<svg class="abs" style="left:0;top:2380px" width="1200" height="60" viewBox="0 0 1200 60"><path d="M0 60 Q600 -10 1200 60 V0 H0Z" fill="#f4ea7b"/></svg>
<svg class="abs ribbon" viewBox="0 0 892 250"><path d="M0 0 L892 0 L842 250 L50 250Z" fill="#2e9a2a"/><path d="M0 0 Q20 30 35 60 L0 60Z" fill="#1d6e1a"/><path d="M892 0 Q872 30 857 60 L892 60Z" fill="#1d6e1a"/></svg>
<div class="abs call-circle"><svg width="64" height="64" viewBox="0 0 24 24"><path fill="#fff" d="M6.6 10.8a15.1 15.1 0 0 0 6.6 6.6l2.2-2.2c.3-.3.7-.4 1-.2 1.1.4 2.3.6 3.6.6.6 0 1 .4 1 1V20c0 .6-.4 1-1 1A17 17 0 0 1 3 4c0-.6.4-1 1-1h3.5c.6 0 1 .4 1 1 0 1.3.2 2.5.6 3.6.1.3 0 .7-.2 1z"/></svg></div>
<p class="abs call-lines call-head">CALL TODAY TO LEARN MORE<br>FROM THE SAFETY OF YOUR HOME:</p>
<p class="abs call-lines call-number">(555) 014-2290</p>

<p class="abs promo">Mention this email and get an additional 5%<br>our Spring Savings with promo code PHSpring2021</p>

<section class="abs location">
  <div class="location-photo" role="img" aria-label="Photo of the cemetery entrance gate with palm trees"></div>
  <div class="location-body">
    <h3 class="location-title">location</h3>
    <p class="location-name">Palm Hollow Memorial Park Cemetery</p>
    <p class="location-line">4800 Harbor Lane<br>Coral Bend, FL 33000</p>
  </div>
</section>

<p class="abs learn">Learn More</p>
<div class="abs social social-web"><svg width="70" height="70" viewBox="0 0 24 24" fill="none" stroke="#fff" stroke-width="1.4"><circle cx="12" cy="12" r="9"/><ellipse cx="12" cy="12" rx="4" ry="9"/><path d="M3 12h18M4.5 7.5h15M4.5 16.5h15"/></svg></div>
<div class="abs social social-follow">Follow</div>
</body>
</html>
```